Real estate company needs a card that makes you say WOW!

We need an awesome business card for our real estate company, Stonebrook Realty Partners of Chicago, that will stand out from the crowd. We specialize in buying and selling real estate, property management, and real estate investments (Flips & Rentals). On the business card, I need the following:

- Our logo
- Services
- My name & contact info (Derek Ollanby, 630-517-2946, Derek@StonebrookRPC.com)
- My title (Director of Acquisitions)
- StonebrookRPC.com

I attached an EPS file of our logo. Let me know if you have any questions. Thank you in advance!

```html
<!DOCTYPE html>
<html lang="en">
<head>
<meta charset="utf-8">
<title>Stonebrook Realty Partners of Chicago – Business Card</title>
<link rel="stylesheet" href="https://fonts.googleapis.com/css2?family=Cinzel:wght@400&family=Open+Sans:wght@400&display=swap">
<style>
  :root {
    --bg: #e9e6e1;
    --card-white: #ffffff;
    --brand-blue: #1a64a8;
    --sky-light: #2a9ad8;
    --sky-deep: #0d4f92;
    --text-grey: #6b6b6b;
    --rule-grey: #9a9a9a;
    --card-black: #0c0c0c;
    --card-black-soft: #2a2a2a;
    --services-grey: #b9b9b9;
  }
  * { box-sizing: border-box; margin: 0; padding: 0; }
  html, body { width: 1200px; height: 1014px; overflow: hidden; }
  body {
    background: var(--bg);
    font-family: "Open Sans", Arial, sans-serif;
    position: relative;
  }
  .card {
    position: absolute;
    left: 250px;
    width: 700px;
    height: 400px;
    overflow: hidden;
    box-shadow: 0 6px 18px rgba(0,0,0,0.18);
  }
  /* Front */
  .card-front { top: 60px; background: var(--card-white); }
  .skyline-area {
    position: absolute;
    left: 0; top: 0;
    width: 100%; height: 170px;
    background: linear-gradient(180deg, var(--sky-light) 0%, var(--sky-deep) 100%);
  }
  .front-info {
    position: absolute;
    left: 0; right: 0; bottom: 60px;
    display: flex;
    align-items: flex-start;
  }
  .identity { width: 360px; padding-left: 70px; }
  .identity .name {
    font-family: "Cinzel", Georgia, serif;
    color: var(--brand-blue);
    font-size: 30px;
    letter-spacing: 0.5px;
    line-height: 1.15;
  }
  .identity .title {
    color: var(--text-grey);
    font-size: 19px;
    margin-top: 2px;
  }
  .divider {
    width: 1px;
    height: 110px;
    background: var(--rule-grey);
    margin-top: -10px;
  }
  .contact {
    padding-left: 26px;
    color: var(--text-grey);
    font-size: 18px;
    line-height: 1.55;
  }
  /* Back */
  .card-back {
    top: 540px;
    background: linear-gradient(160deg, var(--card-black) 0%, var(--card-black-soft) 50%, var(--card-black) 100%);
  }
  .company-name {
    position: absolute;
    left: 0; right: 0; top: 150px;
    text-align: center;
    font-family: "Cinzel", Georgia, serif;
    color: var(--brand-blue);
    font-size: 34px;
    letter-spacing: 2px;
    line-height: 1.3;
  }
  .services {
    position: absolute;
    left: 0; right: 0; bottom: 40px;
    text-align: center;
    color: var(--services-grey);
    font-size: 19px;
    letter-spacing: 0.3px;
  }
</style>
</head>
<body>
  <section class="card card-front">
    <div class="skyline-area" role="img" aria-label="Blue Chicago skyline silhouette"></div>
    <div class="front-info">
      <div class="identity">
        <p class="name">Derek Ollanby</p>
        <p class="title">Director of Acquisitions</p>
      </div>
      <div class="divider"></div>
      <div class="contact">
        <p>630-517-2946</p>
        <p>Derek@StonebrookRPC.com</p>
        <p>StonebrookRPC.com</p>
      </div>
    </div>
  </section>

  <section class="card card-back">
    <p class="company-name">Stonebrook Realty Partners<br>of Chicago</p>
    <p class="services">Sales | Acquisitions | Rentals &amp; Services | Lowns</p>
  </section>
</body>
</html>
```